sailbrightly Website for children with diabilities

Hi, we are looking for a new website design for our community service "sailbrightly". Sailbrightly gives children who suffer from diseases or disabilities a week off on a Boat to give the children new hope and an unforgettable experience.

The current website is really old and we want to have a new one.
Please feel free to discover our website under http://sailbrightly-example.at/.
We have several company sponsors which are very important to us.

The Website has to be a Bootstrap Design (Version 4.4 or higher) [NOT Wordpress, Joomla, other CMS]

Target Market(s)

no target market. we like to inform our communities about our service.

Industry/Entity Type

community service for children with disabilities

Coding

Number of Pages Required

4 page

Font styles to use
Sans Serif

Colors
0054AA
0677BA
7BADD7
CADEEF
E8F1F8
0094D4
00A9DD
6FCCEA
C7EBF8
E9F6FB

Requirements
Must have
• About, Sponsors, Information about cruises
Nice to have
• Gallery

```html
<!DOCTYPE html>
<html lang="en">
<head>
<meta charset="utf-8">
<title>Verein Sail Brightly</title>
<link rel="stylesheet" href="https://fonts.googleapis.com/css2?family=Poppins:wght@400;500;600;700;800&display=swap">
<style>
:root{
  --navy:#161d5c;
  --navy-deep:#131a55;
  --steel:#a9bec8;
  --steel-dark:#98afbb;
  --ink:#2c3560;
  --white:#ffffff;
  --light:#eceef3;
  --circle:#eeeff2;
  --accent-block:#e4e7eb;
  --photo-deep:#1f4f86;
}
*{margin:0;padding:0;box-sizing:border-box}
html,body{width:1200px;height:3460px;overflow:hidden;background:var(--white)}
body{position:relative;font-family:'Poppins',sans-serif;color:var(--navy)}
.abs{position:absolute}
a{color:inherit;text-decoration:none}

/* header */
.brand-mark{left:89px;top:11px;width:96px;height:96px;border-radius:50%;background:var(--navy);display:flex;align-items:center;justify-content:center;color:var(--white);font-weight:600;font-size:13px}
.nav{top:40px;left:0;font-size:14.5px;color:#2a2f55}
.nav a{position:absolute;white-space:nowrap}
.nav .active{color:var(--steel-dark)}
.nav-bar{left:361px;top:0;width:60px;height:3px;background:var(--steel)}
.fleet-btn{left:974px;top:28px;width:136px;height:42px;border-radius:21px;background:var(--light);font-size:12.5px;font-weight:600;display:flex;align-items:center;justify-content:center}

/* hero */
.hero-title{left:88px;top:172px;font-weight:800;font-size:80px;line-height:75px;letter-spacing:-1px;color:var(--navy);white-space:nowrap}
.hero-title .soft{color:var(--steel)}
.hero-tag{left:89px;top:418px;font-size:16px;line-height:23px;color:var(--ink)}
.band{left:0;top:544px;width:1200px;height:744px;background:var(--steel)}
.hero-frame{left:519px;top:93px;width:681px;height:520px;background:var(--white);box-shadow:0 10px 30px rgba(0,0,0,.08)}
.photo{background:linear-gradient(160deg,#3d80b8,var(--photo-deep))}
.hero-photo{left:531px;top:101px;width:669px;height:501px}

.assoc{left:0;top:692px;width:1200px;text-align:center;color:var(--white);font-weight:700;font-size:31px;line-height:40px}

.accent-block{background:var(--accent-block)}
.about-accent{left:161px;top:812px;width:176px;height:176px}
.about-photo{left:180px;top:829px;width:403px;height:503px;background:linear-gradient(180deg,#2d6aa8 0%,#1f5596 60%,#8a5434 78%,#7a4a2e 100%)}
.about-head{left:643px;top:868px;font-size:42px;line-height:45px;font-weight:700;color:var(--white)}
.about-text{left:644px;top:976px;width:380px;font-size:15.5px;line-height:24px;color:var(--white)}
.read-btn{left:644px;top:1144px;width:136px;height:41px;border-radius:21px;background:var(--white);font-size:13px;font-weight:600;display:flex;align-items:center;justify-content:center}

/* accordion */
.acc-item{position:absolute;left:89px;width:530px;font-size:13px;font-weight:600;color:var(--navy)}
.acc-item svg{position:absolute;right:0;top:4px}
.acc-text{left:89px;top:1503px;width:535px;font-size:14px;line-height:22.5px;color:#3b4266}
.acc-rule{left:89px;width:530px;height:1px;background:#dfe2e8}

.sail-accent{left:742px;top:1582px;width:408px;height:407px}
.sail-photo{left:683px;top:1395px;width:427px;height:556px;background:linear-gradient(180deg,#c8d6e8 0%,#9fb8d6 45%,#29518a 62%,#1c3f73 100%)}

/* gallery */
.section-title{left:0;width:1200px;text-align:center;font-weight:800;font-size:40px;color:var(--navy)}
.g-item{top:2106px;width:194px;height:316px}
.g-arrow{top:2230px;width:32px;height:68px;background:#f0f1f4;display:flex;align-items:center;justify-content:center}
.g-icon{top:2239px;width:48px;height:48px;border-radius:50%;background:var(--white);display:flex;align-items:center;justify-content:center}

/* sponsors */
.sponsor{top:2589px;width:164px;height:164px;border-radius:50%;background:var(--circle);display:flex;align-items:center;justify-content:center;font-weight:700;font-size:20px;color:var(--navy)}

/* footer */
.footer{left:0;top:2943px;width:1200px;height:517px;background:var(--navy-deep)}
.newsletter{left:632px;top:2865px;width:568px;height:157px;background:var(--steel)}
.nl-title{left:712px;top:2898px;font-size:17px;font-weight:700;color:var(--white)}
.nl-input{left:712px;top:2932px;width:360px;height:45px;background:var(--white);font-size:14px;color:#555b75;display:flex;align-items:center;padding-left:40px}
.nl-btn{left:1072px;top:2932px;width:38px;height:45px;background:var(--navy);display:flex;align-items:center;justify-content:center}
.foot-brand{left:168px;top:3200px;display:flex;align-items:center;gap:14px;font-size:30px;font-weight:600;color:var(--white)}
.foot-brand span.dot{width:26px;height:26px;border-radius:50%;background:var(--steel)}
.foot-col{top:3108px;color:var(--white)}
.foot-col h4{font-size:17px;font-weight:700;margin-bottom:16px}
.foot-col li{list-style:none;font-size:13px;line-height:31.3px;color:#e6e8f2}
.foot-col li::before{content:"›";margin-right:7px}
.contact-row{font-size:13px;line-height:18px;color:#e6e8f2;display:flex;gap:8px;margin-bottom:17px}
.social{top:3258px;width:42px;height:42px;border-radius:50%;background:#242c6a}
.foot-rule{left:89px;top:3400px;width:1022px;height:1px;background:#323a76}
.copyright{left:0;top:3421px;width:1200px;text-align:center;font-size:13px;color:#e6e8f2}
.to-top{left:1130px;top:3368px;width:40px;height:40px;border-radius:50%;background:var(--steel);display:flex;align-items:center;justify-content:center}
</style>
</head>
<body>

<header>
  <div class="abs brand-mark">sailbrightly</div>
  <div class="abs nav-bar"></div>
  <nav class="abs nav">
    <a class="active" style="left:371px">HOME</a>
    <a style="left:445px">ABOUT</a>
    <a style="left:521px">GALLERY</a>
    <a style="left:609px">SPONSORS</a>
    <a style="left:714px">ABOUT CRUISES</a>
    <a style="left:851px">CONTACT US</a>
  </nav>
  <a class="abs fleet-btn">FLEET INFO 2022</a>
</header>

<section class="hero">
  <div class="abs band"></div>
  <h1 class="abs hero-title">VEREIN<br><span class="soft">SAIL</span><br>BRIGHTLY</h1>
  <p class="abs hero-tag">WE CAN'T TELL THE DIRECTION OF THE WIND,<br>BUT WE CAN SET THE SAILS RIGHT!</p>
  <div class="abs hero-frame"></div>
  <div class="abs photo hero-photo" role="img" aria-label="Two children in life jackets sitting in an inflatable dinghy on the sea"></div>
  <h2 class="abs assoc">REGISTERED ASSOCIATION<br>ZVR NUMBER: 031572846</h2>
</section>

<section class="about">
  <div class="abs accent-block about-accent"></div>
  <div class="abs about-photo" role="img" aria-label="A child and a skipper in crew shirts sitting on the teak stern of a boat watching the wake"></div>
  <h2 class="abs about-head">ABOUT<br>SAIL BRIGHTLY</h2>
  <p class="abs about-text">...trained social workers and experienced skippers who volunteer in the Sail Brightly association and organize a fleet every year for socially disadvantaged children and young people from central Upper Austria and set up the necessary financial resources.</p>
  <a class="abs read-btn">READ MORE</a>
</section>

<section class="values">
  <div class="abs acc-item" style="top:1466px">WE ARE...
    <svg width="10" height="8" viewBox="0 0 10 8"><path d="M1 2l4 4 4-4" fill="none" stroke="#161d5c" stroke-width="1.6"/></svg></div>
  <p class="abs acc-text">...trained social workers and experienced skippers who volunteer in the Sail Brightly association &amp; organize a fleet every year for socially disadvantaged children and young people from central Upper Austria and set up the necessary financial resources.</p>
  <div class="abs acc-rule" style="top:1623px"></div>
  <div class="abs acc-item" style="top:1647px">WE WANT...
    <svg width="6" height="10" viewBox="0 0 6 10"><path d="M1 1l4 4-4 4" fill="none" stroke="#8a90a8" stroke-width="1.2"/></svg></div>
  <div class="abs acc-rule" style="top:1688px"></div>
  <div class="abs acc-item" style="top:1711px">PRACTICAL IMPLEMENTATION OF THE PEDAGOGICAL CONSIDERATIONS
    <svg width="6" height="10" viewBox="0 0 6 10"><path d="M1 1l4 4-4 4" fill="none" stroke="#8a90a8" stroke-width="1.2"/></svg></div>
  <div class="abs acc-rule" style="top:1755px"></div>
  <div class="abs acc-item" style="top:1779px">PROJECT GOALS
    <svg width="6" height="10" viewBox="0 0 6 10"><path d="M1 1l4 4-4 4" fill="none" stroke="#8a90a8" stroke-width="1.2"/></svg></div>
  <div class="abs acc-rule" style="top:1821px"></div>
  <div class="abs acc-item" style="top:1845px">ACHIEVED GOALS
    <svg width="6" height="10" viewBox="0 0 6 10"><path d="M1 1l4 4-4 4" fill="none" stroke="#8a90a8" stroke-width="1.2"/></svg></div>

  <div class="abs accent-block sail-accent"></div>
  <div class="abs sail-photo" role="img" aria-label="A white sailing yacht under sail near a green island coast"></div>
</section>

<section class="gallery">
  <h2 class="abs section-title" style="top:2036px">OUR GALLERY</h2>
  <div class="abs g-arrow" style="left:66px"><svg width="6" height="10" viewBox="0 0 6 10"><path d="M5 1L1 5l4 4" fill="none" stroke="#161d5c" stroke-width="1.4"/></svg></div>
  <div class="abs photo g-item" style="left:98px" role="img" aria-label="Boys in a yellow inflatable dinghy"></div>
  <div class="abs photo g-item" style="left:301px" role="img" aria-label="Children swimming around a white dinghy"></div>
  <div class="abs photo g-item" style="left:503px;background:linear-gradient(160deg,#8fb0cc,#5a82aa)" role="img" aria-label="Children riding a towed inflatable through spray"></div>
  <div class="abs g-icon" style="left:547px"><svg width="18" height="18" viewBox="0 0 18 18"><circle cx="7.5" cy="7.5" r="5" fill="none" stroke="#161d5c" stroke-width="2"/><path d="M11.5 11.5l4 4" stroke="#161d5c" stroke-width="2"/></svg></div>
  <div class="abs g-icon" style="left:602px"><svg width="18" height="18" viewBox="0 0 18 18"><path d="M7.5 10.5l3-3M6 8.5l-2 2a2.8 2.8 0 004 4l2-2M12 9.5l2-2a2.8 2.8 0 00-4-4l-2 2" fill="none" stroke="#161d5c" stroke-width="2" stroke-linecap="round"/></svg></div>
  <div class="abs photo g-item" style="left:705px;background:linear-gradient(180deg,#2aa0b8,#1d5fb0)" role="img" aria-label="A girl doing a handstand on a blue and white float"></div>
  <div class="abs photo g-item" style="left:907px" role="img" aria-label="Girls in orange life vests on a towed tube"></div>
  <div class="abs g-arrow" style="left:1099px"><svg width="6" height="10" viewBox="0 0 6 10"><path d="M1 1l4 4-4 4" fill="none" stroke="#161d5c" stroke-width="1.4"/></svg></div>
</section>

<section class="sponsors">
  <h2 class="abs section-title" style="top:2521px">SPONSORSHIP</h2>
  <div class="abs sponsor" style="left:153px">Lindwerk</div>
  <div class="abs sponsor" style="left:335px">Tavora</div>
  <div class="abs sponsor" style="left:518px">Felsgrund</div>
  <div class="abs sponsor" style="left:700px">wolkenfest</div>
  <div class="abs sponsor" style="left:883px">K. Heinzel</div>
</section>

<footer>
  <div class="abs footer"></div>
  <div class="abs newsletter"></div>
  <h3 class="abs nl-title">SUBSCRIBE OUR NEWSLETTER</h3>
  <div class="abs nl-input">
    <svg class="abs" style="left:17px;top:17px" width="13" height="10" viewBox="0 0 13 10"><rect x=".5" y=".5" width="12" height="9" fill="#9aa0b4"/><path d="M.5 .5l6 5 6-5" fill="none" stroke="#fff"/></svg>
    Enter your email address</div>
  <div class="abs nl-btn"><svg width="13" height="13" viewBox="0 0 13 13"><path d="M12 1L1 6l4 1.5L6.5 12z" fill="#fff"/></svg></div>

  <div class="abs foot-brand"><span class="dot"></span>sailbrightly</div>

  <div class="abs foot-col" style="left:449px">
    <h4>QUICK LINKS</h4>
    <ul><li>Home</li><li>About Us</li><li>Gallery</li><li>Sponsors</li><li>About cruises</li><li>Contact Us</li></ul>
  </div>
  <div class="abs foot-col" style="left:644px">
    <h4>INFORMATION</h4>
    <ul><li>Privacy Policy</li><li>Terms &amp; Conditions</li><li>Shipping Policy</li><li>FAQ's</li><li>About Us</li><li>Blog</li></ul>
  </div>
  <div class="abs foot-col" style="left:839px">
    <h4>CONTACT INFO</h4>
    <div class="contact-row"><svg width="13" height="10" viewBox="0 0 13 10" style="margin-top:4px"><rect width="13" height="10" fill="#c9cde0"/><path d="M0 0l6.5 5L13 0" fill="none" stroke="#131a55"/></svg><div>Email:<br>verein@sailbrightly.at</div></div>
    <div class="contact-row"><svg width="13" height="13" viewBox="0 0 13 13" style="margin-top:3px"><circle cx="6.5" cy="6.5" r="5.5" fill="none" stroke="#c9cde0" stroke-width="1.5"/><path d="M1 6.5h11M6.5 1c-3 3.5-3 7.5 0 11M6.5 1c3 3.5 3 7.5 0 11" fill="none" stroke="#c9cde0"/></svg><div>Website:<br>http://sailbrightly-example.at/</div></div>
  </div>
  <div class="abs social" style="left:838px" aria-label="Social link"></div>
  <div class="abs social" style="left:886px" aria-label="Social link"></div>
  <div class="abs social" style="left:934px" aria-label="Social link"></div>

  <div class="abs foot-rule"></div>
  <a class="abs to-top"><svg width="10" height="6" viewBox="0 0 10 6"><path d="M1 5l4-4 4 4" fill="none" stroke="#fff" stroke-width="1.4"/></svg></a>
  <p class="abs copyright">© SAILBRIGHTLY 2022 ALL RIGHTS RESERVED</p>
</footer>

</body>
</html>
```